Acrylic print memorial plaque for entrance

I need a design for an acrylic print in DIN A0 portrait format or 1.5x DIN A0.

The top 40% should contain the lettering "Veronika's Meadow Haven." The lettering should frame three pictures. In the center is a portrait of Vero (Veronika), with "In Memoriam" below the name and the dates *November 20, 1980 †May 15, 2024. The head of the horse Solvina should be placed on the left, and Bellis's head on the right.
The next 35% of the area should depict the portraits of Gerhard (left), Henrik (middle), and Frieda (right) in the upper part. Each with their name underneath. The lower part of this 35% should contain

“Our helpers:”
Then the portraits of Dieter, Helene, Uschi & Glenn should be taken in the following order. Each one should also have its name underneath the portrait.
The remaining 25% should contain the following:
“We would like to thank:
Klaus & Ingrid for their valuable support, and Hanni for her help and tips on handling the horse. We would also like to thank the Weibel family, especially Beni & Sabine and Flori & Greta, for allowing us to create this paradise according to our ideas and for the construction. And, of course, the many other helpers and supporters.
The images should be isolated as much as possible and scaled to fit the print size. If possible, only the faces (head + neck) should be included.

Cut out, shape, or mirror the horse heads depending on the design.

The various images can be used as backgrounds, provided the design allows it.

Target Market(s)

No target mark, memorial plaque for the stable

Font styles to use
Serif
Decorative
Script

Requirements
Must have
• Honest, Authentic, Devotional
Should not have
• Kitsch, too playful.

```html
<!DOCTYPE html>
<html lang="en">
<head>
<meta charset="utf-8">
<title>Veronika's Meadow Haven – In Memoriam</title>
<link rel="stylesheet" href="https://fonts.googleapis.com/css2?family=Cinzel:wght@400;600&family=Great+Vibes&display=swap">
<style>
  :root {
    --night: #0b0f1c;
    --deep-blue: #121a33;
    --sea: #26406e;
    --sea-light: #4a6a9e;
    --sand: #6a5440;
    --sand-dark: #2a2119;
    --ring: #2f55b5;
    --ring-edge: #e8ecf5;
    --text: #f4f4f6;
    --date: #b9c6e6;
  }
  * { margin: 0; padding: 0; box-sizing: border-box; }
  html, body { width: 855px; height: 1200px; overflow: hidden; background: var(--night); }
  .plaque {
    position: relative; width: 855px; height: 1200px; overflow: hidden;
    background: linear-gradient(180deg, var(--night) 0%, var(--deep-blue) 30%, var(--night) 100%);
    color: var(--text); font-family: "Cinzel", serif;
  }
  .landscape {
    position: absolute; left: 0; top: 330px; width: 855px; height: 700px;
    background: linear-gradient(180deg, var(--deep-blue) 0%, var(--sea) 15%, var(--sea-light) 25%, var(--sea) 36%, var(--sand) 58%, var(--sand-dark) 100%);
    opacity: .85;
  }
  .title {
    position: absolute; top: 18px; left: 0; width: 100%; text-align: center;
    font-size: 44px; font-weight: 400; letter-spacing: 2px;
  }
  .photo {
    position: absolute; border: 8px solid var(--ring);
    box-shadow: 0 0 0 3px var(--ring-edge), 0 6px 18px rgba(0,0,0,.5);
  }
  .oval { border-radius: 50%; }
  .horse-left { left: 34px; top: 100px; width: 246px; height: 256px; background: linear-gradient(160deg, #c9d3de, #3a2e28 55%, #1a1512); }
  .horse-right { left: 575px; top: 100px; width: 246px; height: 256px; background: linear-gradient(200deg, #d9dfe6, #b87a4a 50%, #6e4426); }
  .portrait-main { left: 285px; top: 78px; width: 285px; height: 292px; background: linear-gradient(170deg, #f1f1f3, #8a6a5a 45%, #2a1e1c); z-index: 2; }
  .circle { border-radius: 50%; }
  .row-person { top: 545px; width: 180px; height: 180px; }
  .p-gerhard { left: 67px; background: linear-gradient(160deg, #cfd4da, #9a7f72 55%, #4a4a50); }
  .p-henrik { left: 338px; background: linear-gradient(160deg, #dfe3e8, #a58470 55%, #2e3a4c); }
  .p-frieda { left: 608px; background: linear-gradient(160deg, #d8dbe0, #b08a78 55%, #3c4a5e); }
  .helper { top: 835px; width: 110px; height: 110px; border-width: 5px; box-shadow: 0 0 0 2px var(--ring-edge); }
  .h-dieter { left: 335px; background: linear-gradient(160deg, #7a9a6a, #a57d68 55%, #3a3630); }
  .h-helene { left: 461px; background: linear-gradient(160deg, #8aa0b6, #b08a74 55%, #3c3a44); }
  .h-uschi { left: 586px; background: linear-gradient(160deg, #e9e9ee, #c19a7e 55%, #6a5240); }
  .h-glenn { left: 709px; background: linear-gradient(160deg, #9aa8b8, #b0907c 55%, #4a4a52); }
  .script { position: absolute; font-family: "Great Vibes", cursive; text-align: center; color: var(--text); text-shadow: 0 2px 6px rgba(0,0,0,.6); line-height: 1.2; }
  .name-lg { font-size: 44px; width: 260px; top: 362px; }
  .name-main { font-size: 48px; width: 285px; top: 368px; left: 285px; }
  .name-md { font-size: 40px; width: 220px; top: 732px; }
  .name-sm { font-size: 22px; width: 130px; top: 950px; }
  .memoriam {
    position: absolute; top: 438px; left: 0; width: 100%; text-align: center;
    font-size: 40px; letter-spacing: 1px;
  }
  .dates {
    position: absolute; top: 492px; left: 0; width: 100%; text-align: center;
    font-size: 21px; color: var(--date); letter-spacing: 1px;
  }
  .rule { position: absolute; height: 2px; background: var(--text); opacity: .85; }
  .helpers-label {
    position: absolute; top: 838px; left: 22px; font-size: 34px; font-weight: 600;
  }
  .thanks {
    position: absolute; top: 1000px; left: 28px; width: 800px; text-align: center;
    font-size: 16.5px; line-height: 1.5; letter-spacing: .3px;
  }
</style>
</head>
<body>
<main class="plaque">
  <div class="landscape" role="img" aria-label="Soft beach landscape with sea and sand"></div>

  <h1 class="title">Veronika's Meadow Haven</h1>

  <div class="photo oval horse-left" role="img" aria-label="Head of the horse Solvina"></div>
  <div class="photo oval horse-right" role="img" aria-label="Head of the horse Bellis"></div>
  <div class="photo oval portrait-main" role="img" aria-label="Portrait of Veronika"></div>

  <div class="script name-lg" style="left:27px;">Solvina</div>
  <div class="script name-main">Veronika</div>
  <div class="script name-lg" style="left:568px;">Bellis</div>

  <div class="memoriam">In Memoriam</div>
  <div class="dates">November 20, 1980 †May 15, 2024</div>

  <div class="photo circle row-person p-gerhard" role="img" aria-label="Portrait of Gerhard"></div>
  <div class="photo circle row-person p-henrik" role="img" aria-label="Portrait of Henrik"></div>
  <div class="photo circle row-person p-frieda" role="img" aria-label="Portrait of Frieda"></div>

  <div class="script name-md" style="left:47px;">Gerhard</div>
  <div class="script name-md" style="left:318px;">Henrik</div>
  <div class="script name-md" style="left:588px;">Frieda</div>

  <div class="helpers-label">Our helpers:</div>
  <div class="rule" style="left:22px; top:886px; width:290px;"></div>

  <div class="photo circle helper h-dieter" role="img" aria-label="Portrait of Dieter"></div>
  <div class="photo circle helper h-helene" role="img" aria-label="Portrait of Helene"></div>
  <div class="photo circle helper h-uschi" role="img" aria-label="Portrait of Uschi"></div>
  <div class="photo circle helper h-glenn" role="img" aria-label="Portrait of Glenn"></div>

  <div class="script name-sm" style="left:325px;">Dieter</div>
  <div class="script name-sm" style="left:451px;">Helene</div>
  <div class="script name-sm" style="left:576px;">Uschi</div>
  <div class="script name-sm" style="left:699px;">Glenn</div>

  <p class="thanks">
    We would like to thank:<br>
    Klaus &amp; Ingrid for their valuable support, and Hanni for her help and tips on handling the horse.
    We would also like to thank the Weibel family, especially Beni &amp; Sabine and Flori &amp; Greta,
    for allowing us to create this paradise according to our ideas and for the construction.
    And, of course, the many other helpers and supporters.
  </p>
</main>
</body>
</html>
```